Garden Design Flier

I would like a PDF of this half page A4 flier in soft green tones with dark green leaves.

Target Market(s)

Home owners and real estate agents

Font styles to use
Serif
Other font styles liked:
• Papyrus

Colors
acd136
9bcb3c
cadf82
fefdec

Requirements
Must have
• Green tones
Nice to have
• Leaves, vines, lawns
Should not have
• Open to ideas, but classic style

```html
<!DOCTYPE html>
<html lang="en">
<head>
<meta charset="utf-8">
<title>Verdure Gardens – Garden Design Flier</title>
<link rel="stylesheet" href="https://fonts.googleapis.com/css2?family=Cinzel:wght@400&family=Marcellus&display=swap">
<style>
  :root {
    --leaf-dark: #1d3a1c;
    --leaf-mid: #3f6b2c;
    --meadow: #9bcb3c;
    --meadow-soft: #cadf82;
    --meadow-light: #e4ec9a;
    --cream: #fefdec;
    --ink-green: #1f3f1a;
  }
  html, body {
    margin: 0;
    padding: 0;
    overflow: hidden;
    background: #ffffff;
  }
  .flier {
    position: relative;
    width: 1200px;
    height: 846px;
    overflow: hidden;
    font-family: "Marcellus", serif;
    color: var(--cream);
  }
  .flier__backdrop {
    position: absolute;
    inset: 0;
    width: 100%;
    height: 100%;
  }
  .flier__text {
    position: absolute;
    margin: 0;
    white-space: nowrap;
    font-weight: 400;
  }
  .centered { transform: translateX(-50%); text-align: center; }

  .brand-name {
    left: 601px; top: 22px;
    font-family: "Cinzel", serif;
    font-size: 74px;
    letter-spacing: 15px;
    line-height: 1;
  }
  .brand-sub {
    left: 601px; top: 106px;
    font-family: "Cinzel", serif;
    font-size: 34px;
    letter-spacing: 62px;
    padding-left: 62px;
    line-height: 1;
  }
  .owner-name {
    left: 601px; top: 162px;
    font-size: 25px;
    line-height: 1;
  }
  .business-number {
    left: 607px; top: 216px;
    font-size: 26px;
    line-height: 1;
  }
  .service-step {
    top: 270px;
    font-size: 44px;
    line-height: 1;
    transform: translateX(-50%);
  }
  .service-step--design { left: 120px; }
  .service-step--install { left: 356px; }
  .service-step--grow { left: 603px; }
  .service-step--tend { left: 818px; }
  .service-step--enjoy { left: 1088px; }

  .pitch {
    left: 601px;
    font-size: 24px;
    line-height: 34px;
    color: var(--ink-green);
  }
  .pitch--services { top: 396px; }
  .pitch--bespoke { top: 532px; }

  .contact {
    top: 768px;
    font-size: 31px;
    line-height: 1;
  }
  .contact--email { left: 39px; }
  .contact--mobile { right: 40px; }
</style>
</head>
<body>
<main class="flier">
  <svg class="flier__backdrop" viewBox="0 0 1200 846" role="img" aria-label="Photograph of a dense dark green hedge with a heart-shaped opening revealing a soft, blurred sunlit garden behind" preserveAspectRatio="none">
    <defs>
      <radialGradient id="hedge-glow" cx="0.5" cy="0.5" r="0.62" fx="0.52" fy="0.52">
        <stop offset="0" stop-color="#e4ec9a"/>
        <stop offset="0.22" stop-color="#cadf82"/>
        <stop offset="0.42" stop-color="#8fb84a"/>
        <stop offset="0.62" stop-color="#3f6b2c"/>
        <stop offset="1" stop-color="#1d3a1c"/>
      </radialGradient>
    </defs>
    <rect width="1200" height="846" fill="url(#hedge-glow)"/>
  </svg>

  <h1 class="flier__text brand-name centered">VERDURE</h1>
  <p class="flier__text brand-sub centered">GARDENS</p>
  <p class="flier__text owner-name centered">Elliot Harrow</p>
  <p class="flier__text business-number centered">ABN: 51824093716</p>

  <p class="flier__text service-step service-step--design">Design</p>
  <p class="flier__text service-step service-step--install">Install</p>
  <p class="flier__text service-step service-step--grow">Grow</p>
  <p class="flier__text service-step service-step--tend">Tend</p>
  <p class="flier__text service-step service-step--enjoy">Enjoy</p>

  <p class="flier__text pitch pitch--services centered">All your gardening and landscaping needs<br>from design and installation<br>to general maintainance</p>
  <p class="flier__text pitch pitch--bespoke centered">Bespoke vegetable gardens<br>&amp; potager designs created<br>to suite your site<br>and requirement</p>

  <p class="flier__text contact contact--email">Email: elliot@verduregardens.com.au</p>
  <p class="flier__text contact contact--mobile">Mobile: 0400 318 254</p>
</main>
</body>
</html>
```